Business Card Design Project

The business card is for an educational company that provides personalised tuition to students.

The company logo is in orange and blue (as provided) and should be included in the name card design

The philosophy of the company is to make learning a comfortable experience for student as such design of the namecard should look fresh and has a bit of the 'wow' factor. Some of the namecard design that appeals to me are as uploaded under Sample Design.

The particulars that need to be provided are:
(1): Company Name (Quillmark Education)
(1): Name
(2): Educational qualifications which will appear below name
(3): Mobile number
(4): Email address
(5): Website

Industry/Entity Type

Business

Requirements
Must have
• (1): Company Logo

(2): The card background should preferably be coloured both for the front side and back.

(3): The choice of font is important as part of the selection consideration. There is no preferred font that I have selected, designer is free to choose the font that will complement their design.

```html
<!DOCTYPE html>
<html lang="en">
<head>
<meta charset="utf-8">
<title>Quillmark Education – Business Cards</title>
<link href="https://fonts.googleapis.com/css2?family=Libre+Baskerville:wght@700&family=Questrial&display=swap" rel="stylesheet">
<style>
  :root {
    --page: #e9e6e2;
    --card-black: #1c1a1a;
    --sky: #1f8ad6;
    --sky-light: #5cb8f0;
    --orange: #f07a1a;
    --white: #ffffff;
    --soft-grey: #d8d8d8;
  }
  html, body {
    margin: 0;
    width: 1200px;
    height: 900px;
    overflow: hidden;
    background: var(--page);
  }
  .sheet {
    position: relative;
    width: 1200px;
    height: 900px;
  }
  .card {
    position: absolute;
    left: 290px;
    width: 620px;
    height: 354px;
    border-radius: 22px;
    overflow: hidden;
    background: var(--card-black);
    box-shadow: 0 10px 28px rgba(0,0,0,0.25);
  }
  .card--front { top: 70px; }
  .card--back { top: 476px; }
  .card__art {
    position: absolute;
    inset: 0;
  }
  .brand {
    position: absolute;
    display: flex;
    align-items: center;
    gap: 16px;
    color: var(--white);
    font-family: "Libre Baskerville", Georgia, serif;
    font-weight: 700;
    line-height: 1.05;
  }
  .brand__square {
    border-radius: 12%;
    background: var(--orange);
    flex: none;
  }
  .card--front .brand { left: 92px; top: 128px; font-size: 44px; }
  .card--front .brand__square { width: 96px; height: 96px; }
  .card--back .brand { right: 34px; bottom: 30px; font-size: 24px; gap: 10px; }
  .card--back .brand__square { width: 54px; height: 54px; }
  .brand__name span { display: block; }

  .person {
    position: absolute;
    left: 268px;
    top: 58px;
    font-family: "Questrial", Arial, sans-serif;
    color: var(--soft-grey);
  }
  .person__name {
    margin: 0;
    font-size: 34px;
    font-weight: 400;
    font-variant: small-caps;
    letter-spacing: 1px;
  }
  .person__role {
    margin: 2px 0 14px;
    font-size: 15px;
    letter-spacing: 1px;
    text-transform: uppercase;
  }
  .contacts {
    list-style: none;
    margin: 0;
    padding: 0;
    font-size: 19px;
  }
  .contacts li {
    display: flex;
    align-items: center;
    gap: 12px;
    margin-bottom: 6px;
  }
  .contacts__icon {
    width: 20px;
    height: 20px;
    border-radius: 4px;
    background: var(--orange);
    flex: none;
  }
</style>
</head>
<body>
<main class="sheet">

  <section class="card card--front" aria-label="Card front">
    <svg class="card__art" viewBox="0 0 620 354" aria-hidden="true">
      <defs>
        <linearGradient id="skyFront" x1="0" y1="0" x2="1" y2="1">
          <stop offset="0" stop-color="var(--sky-light)"/>
          <stop offset="1" stop-color="var(--sky)"/>
        </linearGradient>
      </defs>
      <path d="M230 0 C 370 30, 520 120, 620 250 L620 0 Z" fill="url(#skyFront)"/>
      <path d="M200 14 C 350 40, 510 130, 620 262" fill="none" stroke="var(--orange)" stroke-width="12"/>
      <path d="M300 4 C 420 30, 530 90, 600 160" fill="none" stroke="var(--sky-light)" stroke-width="6" opacity="0.8"/>
    </svg>
    <div class="brand">
      <div class="brand__square"></div>
      <div class="brand__name"><span>Quillmark</span><span>Education</span></div>
    </div>
  </section>

  <section class="card card--back" aria-label="Card back">
    <svg class="card__art" viewBox="0 0 620 354" aria-hidden="true">
      <defs>
        <linearGradient id="skyBack" x1="0" y1="0" x2="1" y2="1">
          <stop offset="0" stop-color="var(--sky)"/>
          <stop offset="1" stop-color="var(--sky-light)"/>
        </linearGradient>
      </defs>
      <path d="M0 0 L200 0 C 140 100, 120 230, 170 354 L0 354 Z" fill="url(#skyBack)"/>
      <path d="M210 -4 C 148 100, 128 230, 178 358" fill="none" stroke="var(--orange)" stroke-width="12"/>
      <path d="M140 10 C 100 100, 90 200, 110 300" fill="none" stroke="var(--sky-light)" stroke-width="6" opacity="0.8"/>
    </svg>
    <div class="person">
      <h1 class="person__name">Daniel Hart</h1>
      <p class="person__role">Project Manager</p>
      <ul class="contacts">
        <li>
          <svg class="contacts__icon" viewBox="0 0 20 20" aria-hidden="true"><rect width="20" height="20" rx="4" fill="var(--orange)"/><path d="M5 7 Q10 3 15 7 L13 9 L11 8 L9 8 L7 9 Z M6 11 H14 V15 H6 Z" fill="var(--white)"/></svg>
          <span>0198 765 4321</span>
        </li>
        <li>
          <svg class="contacts__icon" viewBox="0 0 20 20" aria-hidden="true"><rect width="20" height="20" rx="4" fill="var(--orange)"/><text x="10" y="14.5" text-anchor="middle" font-size="13" font-family="Arial, sans-serif" fill="var(--white)">@</text></svg>
          <span>info@quillmarkeducation.com</span>
        </li>
        <li>
          <svg class="contacts__icon" viewBox="0 0 20 20" aria-hidden="true"><rect width="20" height="20" rx="4" fill="var(--orange)"/><circle cx="10" cy="10" r="5.5" fill="none" stroke="var(--white)" stroke-width="1.4"/><path d="M4.5 10 H15.5 M10 4.5 V15.5" stroke="var(--white)" stroke-width="1.2"/></svg>
          <span>www.quillmarkeducation.com</span>
        </li>
      </ul>
    </div>
    <div class="brand">
      <div class="brand__square"></div>
      <div class="brand__name"><span>Quillmark</span><span>Education</span></div>
    </div>
  </section>

</main>
</body>
</html>
```